BRISLEY Homes business card Coral Press

I've been a Real Estate agent since 1988. I left the BIG brokerages 2 years ago and am on my own and need a business card. I love doing graphics, but don't have the bandwidth right now.

Background. I want a card that stands out like I do. I'm the fun guy that always has a joke or funny story, and my clients like me. Something fun, but not too silly.

I don't have a symbol or logo that I'm using on the card now, but need to include something, a Font by itself or a logo? I'm not sure if we need a logo or not. I'm open.
The GREAT design is going to be the basis for the next project of stationary, note pads, and Real Estate FOR SALE & Open House signs.

Single sided card is fine, but I selected a 2 sided just in case that's what it works out to be.

Here we go. If you need anything else. Please let me know. As I think of anything, I'll add that also.

Target Market(s)

My territory is Santa Clara County / Silicon Valley, CA. I tend to work with new buyers buying a condo ($500,000) up to single family home for about $1.5 million. 1st time buyers and also move-up buyers. I haven't worked with multi-million $$ homes .... but wouldn't turn it down. Clients here tend to be White, Latin and now many more Chinese and East Indians. Clients also tend to be high tech, Zentrix, Quill, Mingleverse workers and also non tech people.

Industry/Entity Type

Business

Contact Information for Business Card

CONTENT:
Company: BRISLEY Homes
My name: Harold P. Brisley Jr.
Title: Real Estate Broker
Email: Hal@HaroldBrisley.example
Website: www.HaroldBrisley.example
Phone: (408) 555-0172
BRE # 07390418

Font styles to use
Sans Serif

Requirements
Must have
• Content from above. Something that stands out from the others. Serious enough looking, not stale, maybe a bit fun.

```html
<!DOCTYPE html>
<html lang="en">
<head>
<meta charset="utf-8">
<title>BRISLEY Homes business card</title>
<link rel="stylesheet" href="https://fonts.googleapis.com/css2?family=Lato:wght@400;700;900&family=Satisfy&display=swap">
<style>
  :root {
    --backdrop: #e9e6e1;
    --card: #f4efe7;
    --ink: #2a2623;
    --brand-red: #a3232b;
    --leaf-green: #8dc63f;
    --sun-orange: #f3ac32;
    --web-brown: #8a4b2a;
    --rule: #ffffff;
  }
  * { box-sizing: border-box; margin: 0; padding: 0; }
  html, body {
    width: 1200px; height: 968px; overflow: hidden;
    background: var(--backdrop);
    font-family: "Lato", Arial, sans-serif;
    color: var(--ink);
  }
  .sheet {
    width: 1200px; height: 968px;
    display: flex; flex-direction: column; align-items: center; justify-content: center;
    gap: 56px;
  }
  .card {
    position: relative;
    width: 700px; height: 400px;
    background: var(--card);
    border-radius: 4px;
    box-shadow: 0 10px 28px rgba(0,0,0,.14);
    overflow: hidden;
  }
  .card-swoosh { position: absolute; left: 0; top: 0; width: 700px; height: 400px; }

  .brand { display: flex; align-items: center; gap: 10px; }
  .brand-mark { width: 18px; height: 18px; background: var(--brand-red); }
  .brand-name {
    font-weight: 900; color: var(--brand-red);
    letter-spacing: 2px; text-transform: uppercase;
  }
  .brand-web { color: var(--web-brown); font-weight: 700; letter-spacing: .5px; }

  /* front: contact side */
  .front .holder-name {
    position: absolute; left: 56px; top: 52px;
    font-family: "Satisfy", cursive; font-size: 40px; color: var(--ink);
  }
  .front .holder-title {
    position: absolute; left: 58px; top: 112px;
    font-size: 19px; color: var(--brand-red);
  }
  .front .brand { position: absolute; left: 392px; top: 150px; }
  .front .brand-name { font-size: 26px; }
  .front .contact {
    position: absolute; left: 386px; top: 236px;
    list-style: none; display: flex; flex-direction: column; gap: 12px;
    font-size: 16px;
  }
  .contact li { display: flex; align-items: center; gap: 10px; }
  .contact-icon { width: 26px; height: 26px; flex: none; }

  /* back: logo side */
  .back .brand-block {
    position: absolute; left: 0; top: 128px; width: 700px;
    display: flex; flex-direction: column; align-items: center; gap: 14px;
  }
  .back .brand-mark { width: 26px; height: 26px; }
  .back .brand-name { font-size: 46px; }
  .back .brand-web { font-size: 18px; }
</style>
</head>
<body>
<main class="sheet">

  <section class="card front" aria-label="Card front with contact details">
    <svg class="card-swoosh" viewBox="0 0 700 400" aria-hidden="true">
      <path d="M0 362 C170 358 330 365 480 385 C530 392 570 397 610 400 L0 400 Z" fill="var(--brand-red)"/>
      <path d="M0 336 C170 338 330 353 480 385 C330 366 170 360 0 362 Z" fill="var(--leaf-green)"/>
      <path d="M300 400 C450 362 570 334 700 322 L700 400 Z" fill="var(--sun-orange)"/>
      <path d="M300 400 C450 362 570 334 700 322" fill="none" stroke="var(--rule)" stroke-width="3"/>
    </svg>

    <h1 class="holder-name">Harold P. Brisley Jr.</h1>
    <p class="holder-title">Real Estate Broker</p>

    <div class="brand">
      <span class="brand-mark"></span>
      <span class="brand-name">Brisley Homes</span>
    </div>

    <ul class="contact">
      <li>
        <svg class="contact-icon" viewBox="0 0 26 26" aria-hidden="true">
          <circle cx="13" cy="13" r="13" fill="var(--sun-orange)"/>
          <rect x="6.5" y="8.5" width="13" height="9" rx="1" fill="none" stroke="#fff" stroke-width="1.6"/>
          <path d="M6.5 9 L13 14 L19.5 9" fill="none" stroke="#fff" stroke-width="1.6"/>
        </svg>
        <span>Hal@HaroldBrisley.example</span>
      </li>
      <li>
        <svg class="contact-icon" viewBox="0 0 26 26" aria-hidden="true">
          <circle cx="13" cy="13" r="13" fill="var(--brand-red)"/>
          <path d="M9.5 7 C8 8 7.5 10 9 13 C10.5 16 13 18.5 16 19 C17.5 19.2 18.5 18 19 17 L16.5 15 L15 16 C13.5 15.5 11 13 10.5 11.5 L11.5 10 Z" fill="#fff"/>
        </svg>
        <span>(408) 555-0172 BRE # 07390418</span>
      </li>
    </ul>
  </section>

  <section class="card back" aria-label="Card back with company name">
    <svg class="card-swoosh" viewBox="0 0 700 400" aria-hidden="true">
      <path d="M0 372 C200 366 380 360 560 352 C620 350 670 350 700 350 L700 400 L0 400 Z" fill="var(--brand-red)"/>
      <path d="M0 356 C200 346 380 340 560 340 C620 340 670 342 700 344 L700 352 C600 352 380 360 0 372 Z" fill="var(--leaf-green)"/>
      <path d="M340 340 C470 318 590 300 700 296 L700 344 C600 338 470 336 340 340 Z" fill="var(--sun-orange)"/>
    </svg>

    <div class="brand-block">
      <div class="brand">
        <span class="brand-mark"></span>
        <span class="brand-name">Brisley Homes</span>
      </div>
      <span class="brand-web">www.HaroldBrisley.example</span>
    </div>
  </section>

</main>
</body>
</html>
```